Business Card Design/Stationary Design

We would like designers to submit cool, hip business card designs (plus stationary designs) for a new, upstart software development company located in Toronto.
If you have any questions, please email us.
For inspiration on designs:
http://cardmuse.example/cool-business-cards/
http://layoutnotes.example/2008/05/36-cool-business-cards-you-should%E2%80%99ve-seen.html
http://gigharbor.example/general/18-smokin-hot-business-card-designs/

Card info:

Selvakumar (Selv) Nadarasan

Founder and CEO

47 Brindle Court, Suite 311

Toronto, ON M4K 2T8

Phone: 647-512-7730

Mobile: 416-273-5094

Fax: 647-512-7731

Email: selvakumar.nadarasan@mailbrook.example

www.quendrix.example
Updates

Hi everyone,

In terms of all the designs I have seen so far, here is what I like:

1.  I really like the "back" part of this design.  The "front" looks pretty decent as well, but for the "front", look at #2 on this list.  I like that.

http://www.pitchboard.example/image.aspx?imageLocation=1000_10001_2000_image.jpg&type=design300px&whiteLabelCustId=9999

2. "Side 1" of this I like, the front needs to be reworked.

http://www.pitchboard.example/image.aspx?imageLocation=1000_10002_2000_image.png&type=design300px&whiteLabelCustId=9999

3. http://www.pitchboard.example/image.aspx?imageLocation=1000_10003_2000_image.jpg&type=design300px&whiteLabelCustId=9999

4. http://www.pitchboard.example/image.aspx?imageLocation=1000_10004_2000_image.jpg&type=design300px&whiteLabelCustId=9999

Target Market(s)

We are focused on enterprise customers right now, so businesses with a long-term goal of also reaching out to the consumer market as well.

Industry/Entity Type

Software

Requirements
Must have
• Must look cool, ultra-modern, clean and eye-catching. Must incorporate our logo and the colors found in the logo.

```html
<!DOCTYPE html>
<html lang="en">
<head>
<meta charset="utf-8">
<title>Quendrix Stationery</title>
<link rel="stylesheet" href="https://fonts.googleapis.com/css2?family=PT+Sans:wght@400;700&display=swap">
<style>
  :root {
    --lime: #bfff00;
    --green: #6cdb00;
    --accent: #6fd400;
    --ink: #111111;
    --frame: #9a9a9a;
    --rule: #555555;
    --paper: #ffffff;
  }
  * { margin: 0; padding: 0; box-sizing: border-box; }
  html, body { width: 1200px; height: 909px; overflow: hidden; background: var(--paper); }
  .canvas { position: relative; width: 1200px; height: 909px; font-family: "PT Sans", sans-serif; color: var(--ink); }

  .sheet { position: absolute; border: 1.5px solid var(--frame); border-bottom: none; background: var(--paper); overflow: hidden; }
  .card-front { left: 0; top: 0; width: 512px; height: 308px; }
  .card-back { left: 0; top: 372px; width: 512px; height: 307px; }
  .letterhead { left: 558px; top: 3px; width: 641px; height: 906px; }

  .band { position: absolute; bottom: 0; height: 22px; }
  .band-lime { left: 0; background: var(--lime); }
  .band-green { right: 0; background: var(--green); }
  .card-front .band-lime, .card-back .band-lime { width: 388px; }
  .card-front .band-green, .card-back .band-green { width: 115px; }
  .letterhead .band-lime { width: 517px; height: 21px; }
  .letterhead .band-green { width: 115px; height: 21px; }

  .brand { position: absolute; display: flex; align-items: center; gap: 12px; }
  .brand-dot { border-radius: 50%; background: var(--lime); flex: none; }
  .brand-name { font-family: "PT Sans", sans-serif; font-weight: 400; color: var(--ink); line-height: 1; }

  .card-front .brand { left: 156px; top: 118px; }
  .card-front .brand-dot { width: 50px; height: 50px; }
  .card-front .brand-name { font-size: 40px; }

  .card-back .brand { left: 26px; top: 117px; }
  .card-back .brand-dot { width: 130px; height: 130px; }

  .divider { position: absolute; width: 1px; background: #777; }
  .card-back .divider { left: 192px; top: 54px; height: 187px; }

  .contact { position: absolute; left: 231px; top: 50px; }
  .person-name { font-weight: 700; font-size: 18.5px; color: var(--accent); letter-spacing: 0.1px; line-height: 1; }
  .person-role { font-size: 14.5px; margin-top: 6px; line-height: 1; }
  .details { list-style: none; margin-top: 18px; font-size: 13.5px; line-height: 19.6px; }
  .details .label { color: var(--accent); font-weight: 700; }

  .letterhead .brand { left: 22px; top: 25px; gap: 11px; }
  .letterhead .brand-dot { width: 48px; height: 48px; }
  .letterhead .brand-name { font-size: 38px; }
  .letterhead .divider { left: 252px; top: 35px; height: 48px; background: var(--rule); }
  .letter-info { position: absolute; left: 281px; top: 37px; font-style: normal; font-size: 10.6px; line-height: 15.8px; white-space: nowrap; }
</style>
</head>
<body>
<main class="canvas">
  <section class="sheet card-front" aria-label="Business card front">
    <div class="brand">
      <span class="brand-dot"></span>
      <span class="brand-name">Quendrix</span>
    </div>
    <div class="band band-lime"></div>
    <div class="band band-green"></div>
  </section>

  <section class="sheet card-back" aria-label="Business card back">
    <div class="brand"><span class="brand-dot"></span></div>
    <div class="divider"></div>
    <div class="contact">
      <h1 class="person-name">SELVAKUMAR NADARASAN</h1>
      <p class="person-role">Founder and CEO</p>
      <ul class="details">
        <li><span class="label">T:</span> 647-512-7730</li>
        <li><span class="label">M:</span> 416-273-5094</li>
        <li><span class="label">F:</span> 647-512-7731</li>
        <li><span class="label">W:</span> www.quendrix.example</li>
        <li><span class="label">E:</span> selvakumar.nadarasan@mailbrook.example</li>
        <li><span class="label">A:</span> 47 Brindle Court, Suite 311 Toronto,<br>ON M4K 2T8</li>
      </ul>
    </div>
    <div class="band band-lime"></div>
    <div class="band band-green"></div>
  </section>

  <section class="sheet letterhead" aria-label="Letterhead">
    <div class="brand">
      <span class="brand-dot"></span>
      <span class="brand-name">Quendrix</span>
    </div>
    <div class="divider"></div>
    <address class="letter-info">
      47 Brindle Court, Suite 311 Toronto, ON M4K 2T8<br>
      T: 647-512-7730, M: 416-273-5094, F: 647-512-7731<br>
      W: www.quendrix.example, E:selvakumar.nadarasan@mailbrook.example
    </address>
    <div class="band band-lime"></div>
    <div class="band band-green"></div>
  </section>
</main>
</body>
</html>
```